Wordpress Design Project - Basketball Tournament

We need a wordpress design with 3 unique pages for a youth basketball tournament called The Rumble by the Bay. It will take place on April 20-22. The tournament is hosted by Velocity Hoops a non-profit youth basketball organization in Southern California.

We really like the www.tallpinecourts.example website. We are open to ideas about colors. I would like to see bold graphics to that bleed to the edge of the website. Ultimately the website must have a simple and sleek design.

We plan on having the following webpages. Many of these webpages can use the same design, and we can just change the content.

About
Location
Register
Teams - a list of all teams that are participating and divisions (Elite, Open, HS, Girls, etc)
Media
NYSB Coaches
Club/HS Coaches - This is where we provide info on how to get NYSB certified and how to load the roster online
Schedule
Accommodations

Other websites I like include:
http://www.marcusdwellton.example/
www.vortexprime48.example

This contest is for design only.  If you wish to do the code as well, please provide a separate quote for that.  Please include how long it will take to do the coding.  I will give preference to submissions that have the lowest total price for the design and code.

Thank you,
Derek

All designs must state "NYSB Certified".  This must be prominently displayed.

Target Market(s)

Basketball coaches are our primary target market. Most of the coaches are between 25-45 years old and African-American.

Industry/Entity Type

Non-Profit

Requirements
Must have
• a box or column that will display pictures and/or videos.
Nice to have
• It would be nice to have a

```html
<!DOCTYPE html>
<html lang="en">
<head>
<meta charset="utf-8">
<title>The Rumble by the Bay</title>
<link rel="stylesheet" href="https://fonts.googleapis.com/css2?family=Questrial&family=PT+Sans:wght@400;700&family=Fredoka:wght@600&display=swap">
<style>
:root{
  --page:#141414;
  --header-top:#2a2a2a;
  --header-bottom:#151515;
  --panel-light:#d9d9d9;
  --card-grey:#cfcfcf;
  --card-border:#b5b5b5;
  --box-dark:#333333;
  --box-band:#2a2a2a;
  --box-border:#4a4a4a;
  --accent:#f0a050;
  --accent-deep:#e8923c;
  --text-light:#e6e6e6;
  --text-dim:#bdbdbd;
  --text-mid:#444;
  --link:#2b7bb9;
  --feed-title:#2fa3dc;
  --more-brown:#6a4a2e;
  --rule:#555;
}
*{box-sizing:border-box;margin:0;padding:0}
html,body{width:933px;height:1200px;overflow:hidden;background:var(--page)}
body{position:relative;font-family:"PT Sans",sans-serif;color:var(--text-light)}
.abs{position:absolute}

/* header */
.site-header{left:0;top:0;width:933px;height:124px;background:linear-gradient(var(--header-top),var(--header-bottom));border-bottom:1px solid #000}
.brand{left:44px;top:9px;width:104px;height:108px;display:flex;flex-direction:column;align-items:center;justify-content:center;gap:6px}
.brand-dot{width:58px;height:58px;border-radius:50%;background:var(--accent-deep)}
.brand-name{font-family:"Questrial",sans-serif;font-size:11px;line-height:12px;text-align:center;color:#fff}
.event-dates{right:236px;top:22px;font-family:"Questrial",sans-serif;font-size:20px;color:#e4e4e4;white-space:nowrap}
.event-dates em{font-style:normal;color:var(--accent)}
.search{left:712px;top:22px;width:177px;height:27px;border:1px solid #4a4a4a;border-radius:3px;background:#1a1a1a;font-size:10px;font-style:italic;color:#888;padding:7px 12px}
.search svg{position:absolute;right:8px;top:5px}
.main-nav{left:198px;top:87px;display:flex;white-space:nowrap;font-family:"Questrial",sans-serif;font-size:12px;color:#eee}
.main-nav .sep{margin:0 6px;color:#ccc}
.main-nav .current{color:var(--accent);border-bottom:1px solid var(--accent);padding-bottom:2px}

/* content */
.content{left:40px;top:124px;width:850px;height:986px;background:var(--panel-light)}
.player{left:53px;top:144px;width:496px;height:282px;background:#111;border:2px solid #000}
.player-frame{left:4px;top:4px;width:484px;height:248px;background:radial-gradient(circle at 45% 40%,#9a9a9a,#4a4a4a 70%,#2d2d2d)}
.play-btn{left:218px;top:103px;width:56px;height:38px;border-radius:6px;background:rgba(20,20,20,.85)}
.progress{left:0;top:252px;width:492px;height:6px;background:#555}
.progress i{display:block;width:114px;height:6px;background:#c0161b}
.controls{left:0;top:258px;width:492px;height:20px;background:linear-gradient(#3a3a3a,#1e1e1e);font-size:9px;color:#ddd}
.video-list{left:557px;top:144px;width:322px;height:282px;background:#1b1b1b}
.video-item{left:6px;width:311px;height:88px;background:linear-gradient(#4a4a4a,#333);border:1px solid #555}
.video-thumb{left:8px;top:7px;width:123px;height:71px}
.video-item h4{position:absolute;left:139px;top:12px;font-size:10px;color:var(--accent);font-weight:700}
.video-item p{position:absolute;left:139px;top:28px;width:166px;font-size:9px;line-height:12px;color:#ddd}

.intro{left:60px;top:451px;width:490px;font-family:"Questrial",sans-serif;font-weight:400;font-size:16px;line-height:23px;color:#1e1e1e}

.tourney{left:56px;width:492px;background:var(--box-dark);border:1px solid var(--box-border)}
.tourney-band{left:5px;top:5px;width:480px;height:35px;background:var(--box-band);font-family:"Questrial",sans-serif;font-weight:400;font-size:16px;color:var(--accent);padding:9px 11px}
.division{width:127px}
.division h3{font-family:"Questrial",sans-serif;font-weight:400;font-size:16px;color:var(--accent)}
.division p{margin-top:7px;font-size:10px;line-height:14px;color:var(--text-dim);text-align:justify}
.division .more{display:block;text-align:right;margin-top:9px;padding-right:2px;font-size:10.5px;color:var(--accent);border-bottom:1px solid var(--rule);padding-bottom:5px}
.division .more.plain{border:0}

.gallery{left:56px;top:958px;width:492px;height:142px;background:var(--box-dark);border:1px solid var(--box-border)}
.gallery h2{position:absolute;left:16px;top:13px;font-family:"Questrial",sans-serif;font-weight:400;font-size:14px;color:var(--accent)}
.gallery-arrows{left:454px;top:14px}
.gallery-shot{top:42px;width:146px;height:83px;border-radius:3px}

.card{left:566px;width:306px;background:var(--card-grey);border:1px solid var(--card-border);box-shadow:0 1px 2px rgba(0,0,0,.2)}
.about-card p{font-size:10.5px;line-height:16px;color:var(--text-mid);text-align:justify;padding:0 16px}
.about-card .more{position:absolute;right:50px;top:180px;font-size:11px;color:var(--more-brown)}
.court-ball{right:-10px;top:164px;width:44px;height:40px;border-radius:6px;background:linear-gradient(#c06a2a,#8a5a30)}
.feed-title{left:573px;top:677px;font-family:"Fredoka",sans-serif;font-weight:600;font-size:24px;color:var(--feed-title)}
.feed-item{left:12px;width:276px;padding-left:16px;font-size:10.5px;line-height:16px;color:var(--text-mid);text-align:justify}
.feed-item svg{position:absolute;left:0;top:4px}
.feed-item a{color:var(--link);text-decoration:none}
.feed-item .more{position:absolute;right:8px;top:42px;font-size:11px;color:var(--more-brown)}
.tournaments h2{position:absolute;left:14px;top:10px;font-family:"Questrial",sans-serif;font-weight:400;font-size:14px;color:#222}
.badge{width:52px;height:52px;border-radius:50%;background:#a9a9a9;border:2px solid #8e8e8e}

/* footer */
.footer-nav{left:0;top:1127px;width:933px;text-align:center;font-size:10.5px;color:#ccc;white-space:nowrap}
.footer-nav .sep{margin:0 8px}
.copyright{left:55px;top:1163px;font-size:10px;color:#ccc}
.social{right:45px;top:1158px;display:flex;gap:10px;font-size:9px;color:#ccc;align-items:center}
.social span{display:flex;align-items:center;gap:3px}
.social i{width:10px;height:10px;border-radius:50%;background:#5d7fb0;display:inline-block}
</style>
</head>
<body>

<header class="site-header abs">
  <div class="brand abs"><span class="brand-dot"></span><span class="brand-name">The Rumble<br>by the Bay</span></div>
  <div class="event-dates abs">April <em>20</em> - April <em>22</em>, 2012</div>
  <div class="search abs">Search
    <svg width="16" height="16" viewBox="0 0 16 16"><circle cx="6.5" cy="6.5" r="4.5" fill="none" stroke="#bbb" stroke-width="2"/><path d="M10 10l4.5 4.5" stroke="#bbb" stroke-width="2.5" stroke-linecap="round"/></svg>
  </div>
  <nav class="main-nav abs">
    <span class="current">About</span><span class="sep">|</span><span>Location</span><span class="sep">|</span><span>Register</span><span class="sep">|</span><span>Teams</span><span class="sep">|</span><span>Media</span><span class="sep">|</span><span>NYSB Coaches</span><span class="sep">|</span><span>Club/HS Coaches</span><span class="sep">|</span><span>Schedule</span><span class="sep">|</span><span>Accommodations</span>
  </nav>
</header>

<main>
  <div class="content abs"></div>

  <section class="player abs">
    <div class="player-frame abs" role="img" aria-label="Video still of a player rising to dunk a basketball against a grey backdrop"></div>
    <div class="play-btn abs"><svg width="56" height="38" viewBox="0 0 56 38"><path d="M22 10l14 9-14 9z" fill="#fff"/></svg></div>
    <div class="progress abs"><i></i></div>
    <div class="controls abs">
      <svg class="abs" style="left:14px;top:5px" width="10" height="10"><rect x="1" y="1" width="3" height="8" fill="#ddd"/><rect x="6" y="1" width="3" height="8" fill="#ddd"/></svg>
      <svg class="abs" style="left:48px;top:4px" width="14" height="12"><path d="M1 4h3l4-3v10l-4-3H1z" fill="#ddd"/><path d="M10 3q3 3 0 6" stroke="#ddd" fill="none"/></svg>
      <span class="abs" style="left:76px;top:5px"><b>0:02</b> / 0:10</span>
      <span class="abs" style="left:420px;top:5px">720p</span>
      <svg class="abs" style="left:452px;top:4px" width="12" height="12"><path d="M2 10V4h8M7 1l3 3-3 3" stroke="#ddd" fill="none"/></svg>
      <svg class="abs" style="left:474px;top:4px" width="12" height="12"><path d="M1 4V1h3M8 1h3v3M11 8v3H8M4 11H1V8" stroke="#ddd" fill="none"/></svg>
    </div>
  </section>

  <section class="video-list abs">
    <article class="video-item abs" style="top:5px">
      <div class="video-thumb abs" role="img" aria-label="Video thumbnail of a player dunking at the hoop under a blue sky" style="background:linear-gradient(#2f6fb0,#1d4a80)"></div>
      <h4>Excepteur occaecat cupidatat</h4>
      <p>non proident, sunt in culpaqui officia nt mollit anim id est laborum lore eu fugiat pariatur.</p>
    </article>
    <article class="video-item abs" style="top:97px">
      <div class="video-thumb abs" role="img" aria-label="Video thumbnail of a basketball dropping through the net" style="background:radial-gradient(circle at 30% 60%,#8a4a20,#050505 60%)"></div>
      <h4>Excepteur occaecat cupidatat</h4>
      <p>non proident, sunt in culpaqui officia nt mollit anim id est laborum lore eu fugiat pariatur.</p>
    </article>
    <article class="video-item abs" style="top:190px">
      <div class="video-thumb abs" role="img" aria-label="Video thumbnail of two girls competing for the ball" style="background:linear-gradient(90deg,#6a3a7a,#c8a040 55%,#b23a3a)"></div>
      <h4>Excepteur occaecat cupidatat</h4>
      <p>non proident, sunt in culpaqui officia nt mollit anim id est laborum lore eu fugiat pariatur.</p>
    </article>
  </section>

  <h1 class="intro abs">This is an NYSB Certified Event for Boys and Girls High school teams held during the live viewing period</h1>

  <section class="tourney abs" style="top:507px;height:265px">
    <h2 class="tourney-band abs">Boy’s Tournament</h2>
    <div class="division abs" style="left:10px;top:50px"><h3>14 u</h3><p>Excepteur sint cupidatat non proident, sunt in culpa qui officia deserunt</p><span class="more">View more</span></div>
    <div class="division abs" style="left:175px;top:50px"><h3>15 u</h3><p>Excepteur sint cupidatat non proident, sunt in culpa qui officia deserunt</p><span class="more">View more</span></div>
    <div class="division abs" style="left:340px;top:50px"><h3>16 u</h3><p>Excepteur sint cupidatat non proident, sunt in culpa qui officia deserunt</p><span class="more">View more</span></div>
    <div class="division abs" style="left:10px;top:157px"><h3>17 u</h3><p>Excepteur sint cupidatat non proident, sunt in culpa qui officia deserunt</p><span class="more plain">View more</span></div>
  </section>

  <section class="tourney abs" style="top:781px;height:167px">
    <h2 class="tourney-band abs">Girl’s Tournament</h2>
    <div class="division abs" style="left:10px;top:50px"><h3>15 u</h3><p>Excepteur sint cupidatat non proident, sunt in culpa qui officia deserunt</p><span class="more plain">View more</span></div>
    <div class="division abs" style="left:175px;top:50px"><h3>16 u</h3><p>Excepteur sint cupidatat non proident, sunt in culpa qui officia deserunt</p><span class="more plain">View more</span></div>
    <div class="division abs" style="left:340px;top:50px"><h3>17 u</h3><p>Excepteur sint cupidatat non proident, sunt in culpa qui officia deserunt</p><span class="more plain">View more</span></div>
  </section>

  <section class="gallery abs">
    <h2>Our Gallery</h2>
    <svg class="gallery-arrows abs" width="24" height="12" viewBox="0 0 24 12"><path d="M8 1L3 6l5 5M16 1l5 5-5 5" stroke="#fff" stroke-width="2.2" fill="none"/></svg>
    <div class="gallery-shot abs" style="left:15px;background:linear-gradient(#6a5a50,#c0504a)" role="img" aria-label="Game action photo of a player driving to the basket in a crowded arena"></div>
    <div class="gallery-shot abs" style="left:173px;background:linear-gradient(#4a3a30,#8a2a2a 60%,#d8c8b0)" role="img" aria-label="Game action photo of players in maroon and white contesting a shot"></div>
    <div class="gallery-shot abs" style="left:331px;background:radial-gradient(circle at 50% 45%,#e08a30,#3a2010 35%,#0a0a0a 70%)" role="img" aria-label="Close-up of a basketball on a dark court"></div>
  </section>

  <aside>
    <section class="card about-card abs" style="top:458px;height:207px">
      <p style="margin-top:18px">Consectetur adipisicing elit, sed do eiusmod tempor incididunt ut labore et dolore magna aliqua. Ut enim ad minim veniam, quis nostrud exercitation ullamco laboris nisi ut aliquip ex ea commodo consequat. Duis aute irure dolor in reprehenderit in voluptate velit esse cillum dolore eu fugiat nulla pariatur</p>
      <p style="margin-top:14px">, nisi ut aliquid ex ea commodi consequatur? Quis autem vel eum iure reprehenderit qui in ea voluptate velit esse quam nihil molestiae consequatur.</p>
      <span class="more">View more</span>
      <div class="court-ball abs" role="img" aria-label="Small illustration of a basketball resting on a court"></div>
    </section>

    <section class="card abs" style="top:690px;height:207px">
      <div class="feed-item abs" style="top:36px"><svg width="8" height="9"><path d="M0 0l8 4.5L0 9z" fill="#333"/></svg>Anisi ut aliquid ex ea commodi consequatur? Quis autem <a>http://www.rbtb.example/tornmnt/sdjk/58sd</a> ea voluptate velit esse quam.<span class="more">View more</span></div>
      <div class="feed-item abs" style="top:121px"><svg width="8" height="9"><path d="M0 0l8 4.5L0 9z" fill="#333"/></svg>Anisi ut aliquid ex ea commodi consequatur? Quis autem <a>http://www.rbtb.example/tornmnt/sdjk/58sd</a> ea voluptate velit esse quam.<span class="more">View more</span></div>
    </section>
    <h2 class="feed-title abs">Chirp Feeds</h2>

    <section class="card tournaments abs" style="top:926px;height:172px">
      <h2>Tournaments</h2>
      <div class="badge abs" style="left:35px;top:45px"></div>
      <div class="badge abs" style="left:119px;top:45px"></div>
      <div class="badge abs" style="left:207px;top:43px"></div>
      <div class="badge abs" style="left:35px;top:110px"></div>
      <div class="badge abs" style="left:119px;top:110px"></div>
      <div class="badge abs" style="left:207px;top:105px"></div>
    </section>
  </aside>
</main>

<footer>
  <nav class="footer-nav abs">
    <span>About</span><span class="sep">|</span><span>Location</span><span class="sep">|</span><span>Register</span><span class="sep">|</span><span>Teams</span><span class="sep">|</span><span>Media</span><span class="sep">|</span><span>NYSB Coaches</span><span class="sep">|</span><span>Club/HS Coaches</span><span class="sep">|</span><span>Schedule</span><span class="sep">|</span><span>Accommodations</span>
  </nav>
  <p class="copyright abs">Copyright © 2012 www.rumblebythebay.example &nbsp; All rights reserved</p>
  <div class="social abs">
    <span><i></i>Pagebook</span><span><i></i>Chirp</span><span><i></i>LinkUp</span><span><i></i>TubeCast</span>
  </div>
</footer>

</body>
</html>
```